zVerda Corporate Website

zVerda is a well-funded start up developing an Online Marketing Platform for small businesses in Europe.
We are launching in February 2012 with all-in-one online marketing services including professional website, DIY SEO, Dashboard with Reports and Online marketing tools, and Support.
Our internal web designer has come up with a preliminary website design which we wish to continue to improve using new ideas, colours, layout, image, etc.
The brief is very simple - improve the website whether it is look & feel, ease of use, conversion rate - we are looking for overall improvements.
The contest will last 5 days and we will award the winner £300.
If you are the winner , you will also be required to provide designs for 3 more internal pages adhering to the proposed home page design.
Judging criteria : -
Visual Design
Layout must adhere to best practices and wire frame. If you decide to move elements around significantly please provide reason
Functional, informative and drives calls to action
Industry/Entity Type
Marketing
Look and feel
Each slider illustrates characteristics of the customer's brand and the style your logo design should communicate.

```html
<!DOCTYPE html>
<html lang="en">
<head>
<meta charset="utf-8">
<title>zVerda – Online Marketing for Small Businesses</title>
<link href="https://fonts.googleapis.com/css2?family=Arimo:wght@400;700&family=Archivo+Black&display=swap" rel="stylesheet">
<style>
:root{
  --blue-deep:#3f5f93;
  --blue-mid:#5676ab;
  --blue-light:#7f9cc8;
  --sky:#8fd3f2;
  --nav-muted:#a9c3e0;
  --white:#ffffff;
  --ink:#1c1c1c;
  --teal:#1f7f86;
  --teal-bright:#35b6d4;
  --grey-card:#b9bcc2;
}
*{margin:0;padding:0;box-sizing:border-box}
html,body{width:923px;height:1200px;overflow:hidden}
body{
  position:relative;
  font-family:"Arimo",Arial,sans-serif;
  color:var(--white);
  background:linear-gradient(180deg,var(--blue-deep) 0,var(--blue-mid) 98px,#6c8cbf 300px,var(--blue-mid) 470px,#4b6aa0 700px,#46669c 1200px);
}
.abs{position:absolute}

/* header */
.site-header{left:0;top:0;width:923px;height:98px;border-bottom:1px solid #8aa6cf;background:linear-gradient(180deg,#3a5a8e,#4b6ca3)}
.util-nav{right:20px;top:13px;font-size:12px;font-weight:700;display:flex;gap:13px;letter-spacing:.2px}
.brand{left:40px;top:38px;display:flex;align-items:center;gap:10px}
.brand-dot{width:46px;height:46px;border-radius:50%;background:var(--sky)}
.brand-name{font-size:44px;font-weight:400;color:var(--sky);letter-spacing:.5px}
.main-nav{left:286px;top:62px;display:flex;gap:22px;font-size:23px;font-weight:700}
.main-nav span{color:var(--nav-muted)}
.main-nav .current{color:var(--white);position:relative}
.main-nav .current::after{content:"";position:absolute;left:50%;bottom:-13px;margin-left:-8px;border:8px solid transparent;border-bottom-color:#6c8cbf;border-top:0}

/* hero */
.slider-arrow{top:240px}
.showcase{left:54px;top:152px;width:518px;height:194px;border-radius:3px;
  background:linear-gradient(90deg,#9fb7d6 0,#e9eef5 25%,#f4f4f4 50%,#e3eaf3 75%,#a5bad6 100%);
  box-shadow:0 10px 18px rgba(0,0,0,.25)}
.showcase-center{left:185px;top:154px;width:252px;height:190px;
  background:linear-gradient(180deg,#2b2b2b 0,#2b2b2b 18%,#f6f6f6 18%,#ececec 100%);
  border:3px solid #fff;box-shadow:0 6px 16px rgba(0,0,0,.35)}
.features{left:635px;top:156px;list-style:none;font-size:19px;font-weight:700;line-height:23px;color:#e9f1fb}
.features li{padding-left:29px;position:relative}
.features li::before{content:"";position:absolute;left:2px;top:9px;border:9px solid transparent;border-bottom:8px solid #c9d6e8;border-top:0}
.tagline{left:635px;top:270px;font-size:19px;font-weight:700;line-height:23px;color:#dbe6f4}
.signup-band{left:595px;top:323px;width:328px;height:83px;
  background:radial-gradient(ellipse 55% 60% at 55% 55%,var(--teal-bright) 0,#1b5e75 45%,#0e1c26 100%);
  text-align:center}
.signup-band small{display:block;margin-top:18px;font-size:12px;font-weight:700;margin-left:32px}
.signup-band strong{display:block;font-size:38px;line-height:34px;margin-left:32px}
.how{left:54px;top:405px;width:612px;font-size:15px;font-weight:700;line-height:15.5px}
.how h2{font-size:16px;letter-spacing:.4px}

/* headline band */
.headline-band{left:0;top:491px;width:923px;height:55px;text-align:center;
  background:linear-gradient(90deg,#6f8dbd 0,#f4f6f9 12%,#ffffff 50%,#f1f4f8 85%,#7593c2 100%)}
.headline-band h1{font-size:22px;color:var(--ink);margin-top:5px}
.headline-band p{font-size:18px;font-weight:700;color:var(--teal);letter-spacing:.4px}

/* packages */
.package{top:568px;height:193px;overflow:hidden;color:var(--ink);font-family:"Archivo Black","Arial Black",sans-serif;
  background:linear-gradient(90deg,rgba(90,110,150,.0) 0,var(--grey-card) 8%,#d0d2d6 55%,#a7abb3 100%)}
.package .wedge{position:absolute;left:0;top:0;width:100%;height:100%}
.package .t{position:absolute;line-height:1}
.package .plain{font-family:"Arimo",Arial,sans-serif;font-weight:400}
.package .price{color:var(--white);font-size:31px}
.package .lbl{color:var(--white);font-size:14px;text-align:center;line-height:15px}
.outline{color:var(--white);-webkit-text-stroke:1.5px var(--ink);paint-order:stroke fill}

/* quote + newsletter */
.quote{left:60px;top:785px;width:820px;font-size:16.5px;line-height:15.5px;color:#e6ecf5}
.newsletter-label{left:633px;top:834px;font-size:15.5px;font-weight:700}
.newsletter-input{left:639px;top:856px;width:216px;height:36px;border:0;background:linear-gradient(180deg,#fff 60%,#dcdfe6)}

/* tabs */
.tabs{left:0;top:974px;width:923px;height:92px;
  background:linear-gradient(90deg,#7f9cc8 0,#eef0f3 8%,#f4f4f4 50%,#eef0f3 92%,#7f9cc8 100%);color:var(--ink)}
.tabs .rule{position:absolute;left:0;top:34px;width:923px;height:1px;background:#8a8f98}
.tab{position:absolute;top:0;width:210px}
.tab h3{font-size:19px;font-weight:700;color:#8a8d92;padding-top:4px}
.tab.active h3{color:var(--ink)}
.tab.active h3::after{content:"";position:absolute;left:70px;top:28px;border:6px solid transparent;border-bottom-color:#555;border-top:0}
.tab p{position:absolute;top:42px;font-size:16px;font-weight:700;line-height:14.5px;width:210px}
.footer-links{left:0;top:1096px;width:923px;text-align:center;font-size:15.5px;font-weight:700;line-height:19px}
</style>
</head>
<body>

<header class="site-header abs">
  <nav class="util-nav abs"><span>ABOUT US</span><span>CONTACT US</span><span>LOGIN</span></nav>
  <div class="brand abs"><span class="brand-dot"></span><span class="brand-name">zVerda</span></div>
  <nav class="main-nav abs"><span class="current">Home</span><span>Quick Tour</span><span>Pricing</span></nav>
</header>

<svg class="slider-arrow abs" style="left:28px" width="16" height="46" viewBox="0 0 16 46"><path d="M16 0 L0 23 L16 46 Z" fill="#2c2c2c"/></svg>
<svg class="slider-arrow abs" style="left:580px" width="16" height="46" viewBox="0 0 16 46"><path d="M0 0 L16 23 L0 46 Z" fill="#1e1e1e"/></svg>

<div class="showcase abs" role="img" aria-label="Carousel of sample small business website screenshots"></div>
<div class="showcase-center abs" role="img" aria-label="Featured business website template screenshot"></div>

<ul class="features abs">
  <li>Business Websites</li>
  <li>Online Marketing</li>
  <li>Dashboard Controls</li>
  <li>Full Setup &amp; Support</li>
</ul>
<p class="tagline abs">Getting a website has never<br>been so simple!</p>
<div class="signup-band abs"><small>Sign up Now for</small><strong>FREE!</strong></div>

<section class="how abs">
  <h2>HOW DOES IT WORK?</h2>
  <p>Pellentesque habitant morbi tristique senectus et netus et malesuada fames ac turpis egestas. In posuere felis nec tortor. Pellentesque faucibus. Ut ac-cumsan ultricies elit. Maecenas at justo id velit placerat molestie. Donec</p>
</section>

<div class="headline-band abs">
  <h1>The Complete Online Marketing Solution for Small Business Websites</h1>
  <p>“Get a big online presence and more sales leads in 30 minutes”</p>
</div>

<!-- Free setup -->
<div class="package abs" style="left:28px;width:305px">
  <svg class="wedge" viewBox="0 0 305 193" preserveAspectRatio="none"><defs><linearGradient id="w1" x1="0" y1="1" x2="1" y2="0"><stop offset="0" stop-color="#0c0c0c"/><stop offset=".55" stop-color="#1a4a5a"/><stop offset="1" stop-color="#3fc0dc"/></linearGradient></defs><path d="M130 193 L305 40 L305 193 Z" fill="url(#w1)"/></svg>
  <span class="t" style="left:88px;top:28px;font-size:42px;transform:rotate(-3deg)">FREE</span>
  <span class="t outline" style="left:124px;top:64px;font-size:32px">SETUP</span>
  <span class="t plain" style="left:78px;top:126px;font-size:19px;line-height:20px">Web offer<br>only</span>
  <span class="t lbl" style="left:214px;top:142px">value</span>
  <span class="t price" style="left:195px;top:158px">£199</span>
</div>

<!-- Pro package -->
<div class="package abs" style="left:323px;width:296px">
  <svg class="wedge" viewBox="0 0 296 193" preserveAspectRatio="none"><path d="M112 193 L296 40 L296 193 Z" fill="url(#w1)"/></svg>
  <span class="t" style="left:36px;top:18px;font-size:31px;transform:rotate(-8deg)">PRO</span>
  <span class="t" style="left:42px;top:50px;font-size:23px;transform:rotate(-8deg)">PACKAGE</span>
  <span class="t outline" style="left:96px;top:64px;font-size:22px">Big online</span>
  <span class="t outline" style="left:103px;top:84px;font-size:22px">presence</span>
  <span class="t plain" style="left:34px;top:112px;font-size:18px;line-height:15px;text-align:center">&nbsp;&nbsp;&nbsp;Business<br>Website &amp; Easy<br>&nbsp;&nbsp;Dashboard</span>
  <span class="t lbl" style="left:220px;top:118px">per<br>month</span>
  <span class="t price" style="left:196px;top:150px">£22</span>
</div>

<!-- Turbo -->
<div class="package abs" style="left:609px;width:292px">
  <svg class="wedge" viewBox="0 0 292 193" preserveAspectRatio="none"><path d="M108 193 L292 40 L292 193 Z" fill="url(#w1)"/></svg>
  <span class="t" style="left:42px;top:18px;font-size:20px;line-height:19px;transform:rotate(-8deg)">TURBO<br>SALES<br>PRO PLUS</span>
  <span class="t outline" style="left:95px;top:70px;font-size:22px;line-height:19px">More sales<br>&nbsp;&nbsp;leads</span>
  <span class="t plain" style="left:22px;top:116px;font-size:17px;line-height:15px">Business Website,<br>Easy Dashboard &amp;<br>&nbsp;PPC Sales</span>
  <span class="t lbl" style="left:216px;top:116px">per<br>month</span>
  <span class="t price" style="left:205px;top:146px">£29</span>
</div>

<p class="quote abs">“Mauris vel lacus vitae felis vestibulum volutpat. Etiam est nunc, venenatis in, tristique eu, imperdiet ac, nisl. Cum sociis natoque penatibus et magnis dis parturient montes, nascetur ridiculus mus. In iaculis facilisis massa.”</p>
<p class="newsletter-label abs">Sign up for monthly newsletter</p>
<div class="newsletter-input abs" aria-label="Email address field"></div>

<section class="tabs abs">
  <div class="rule"></div>
  <div class="tab active" style="left:65px"><h3 style="padding-left:16px">Case Studies</h3><p>Read real stories about small businesses online.</p></div>
  <div class="tab" style="left:267px"><h3 style="padding-left:55px">How to</h3><p>Learn from our online marketing tips for small businesses.</p></div>
  <div class="tab" style="left:494px"><h3 style="padding-left:3px">News &amp; Chatter</h3><p>Get up-to-date news and chatter about online marketing.</p></div>
  <div class="tab" style="left:690px"><h3 style="padding-left:57px">Demo</h3><p style="width:190px">Find out what zVerda can do for your busi-ness.</p></div>
</section>

<nav class="footer-links abs">
  / Search Marketing - Organic/Natural (SEO) / Social Media / Web Analytics / Contact us /<br>
  / Customer Support / Request a call back / FAQ’s / Site Map / Terms and Conditions /
</nav>

</body>
</html>
```